New Website

New website is to be the same as Valiant Oak.

Website needs to be fully functional, with only text and logo to be added by client at a later date.

Logo has been added for reference.

Coding

Coded - Design and coding required

```html
<!DOCTYPE html>
<html lang="en">
<head>
<meta charset="utf-8">
<title>Corvane</title>
<link href="https://fonts.googleapis.com/css2?family=Open+Sans:ital,wght@0,300;0,400;0,600;1,400&display=swap" rel="stylesheet">
<style>
:root{
  --brand:#3f4fa3;
  --brand-light:#6fa8dc;
  --text:#555;
  --muted:#777;
  --dark:#2b2b2b;
  --darker:#1f1f1f;
  --panel:#f3f2f0;
  --line:#dcdcdc;
  --footer-text:#b8b8b8;
}
*{box-sizing:border-box;margin:0;padding:0}
html,body{width:778px;height:1200px;overflow:hidden;background:#fff}
body{position:relative;font-family:"Open Sans",Arial,sans-serif;color:var(--text)}
.abs{position:absolute}

/* header */
.brand-mark{left:77px;top:24px;width:40px;height:40px;border-radius:50%;background:var(--brand)}
.brand-name{left:130px;top:27px;font-size:29px;font-weight:400;color:var(--brand);letter-spacing:1px;line-height:34px}
.btn-login,.btn-register{top:22px;height:20px;font-size:9.5px;line-height:20px;text-align:center;color:#fff}
.btn-login{left:593px;width:47px;background:#8bbde3}
.btn-register{left:645px;width:56px;background:var(--brand)}
.nav{top:56px;left:0;width:700px;font-size:9.5px;color:#888}
.nav span{position:absolute;top:0;white-space:nowrap}
.nav .active{color:var(--brand)}

/* hero */
.hero-band{left:0;top:108px;width:778px;height:240px;background:#2a2a2a}
.hero{left:76px;top:88px;width:624px;height:280px;background:linear-gradient(180deg,#f4f1ef 0%,#e8e5e3 55%,#cdd2d8 100%);box-shadow:0 10px 12px -8px rgba(0,0,0,.35)}
.hero-photo{left:360px;top:10px;width:264px;height:270px;background:radial-gradient(ellipse at 55% 45%,#6b6e73 0%,#9a9b9f 40%,rgba(230,228,226,0) 72%)}
.hero h1{left:42px;top:68px;font-size:18px;font-weight:400;color:var(--brand)}
.hero p{left:42px;top:101px;width:245px;font-size:9.3px;line-height:16px;color:#333}
.hero .read-more{left:42px;top:151px;width:72px;height:26px;background:#444;color:#fff;font-size:8.5px;line-height:26px;text-align:center}
.dots{left:283px;top:245px;width:58px;height:13px;border-radius:7px;background:#555;display:flex;justify-content:space-around;align-items:center;padding:0 5px}
.dots i{width:5px;height:5px;border-radius:50%;background:#fff}
.dots i:first-child{background:none;border:1px solid #fff}

/* welcome */
.section-title{left:0;width:778px;text-align:center;font-size:19.5px;font-weight:400;color:var(--brand)}
.welcome-text{left:118px;top:430px;width:542px;text-align:center;font-size:9.3px;line-height:17px;color:var(--muted)}
.rule{left:76px;top:509px;width:624px;height:1px;background:var(--line)}

/* services */
.service{top:592px;width:180px;text-align:center}
.service svg{display:block;margin:0 auto}
.service h3{margin-top:14px;font-size:12.5px;font-weight:400;color:var(--brand)}
.service p{margin-top:6px;font-size:7.8px;line-height:13.5px;color:var(--muted)}

/* team */
.team{left:76px;top:737px;width:624px;height:215px;background:var(--panel)}
.member{top:57px;width:105px;height:144px;background:#fff;border:1px solid #e6e6e6;text-align:center}
.member .photo{margin:4px 4px 0;height:94px;background:linear-gradient(180deg,#eceff2,#cfc8c2)}
.member .name{margin-top:14px;font-size:8px;color:var(--brand)}
.member .role{font-size:7.8px;color:var(--muted);margin-top:1px}

/* footer */
.footer{left:0;top:970px;width:778px;height:160px;background:var(--dark)}
.footer h4{position:absolute;top:24px;font-size:14px;font-weight:400;color:#fff}
.footer .txt{position:absolute;top:56px;font-size:8.5px;line-height:13.5px;color:var(--footer-text)}
.footer .divider{position:absolute;top:26px;width:1px;height:106px;background:#444}
.quote{font-style:italic;width:146px;line-height:14.5px!important}
.links li{list-style:none;font-size:7.8px;line-height:17.3px}
.links li::before{content:"•";margin-right:6px}
.email{position:absolute;left:578px;top:51px;width:122px;height:21px;background:#fff;border-radius:2px;font-size:7px;color:#999;line-height:21px;padding-left:8px}
.email b{position:absolute;right:0;top:0;width:27px;height:21px;background:#ddd;border-radius:0 2px 2px 0}
.social{position:absolute;top:112px;width:11px;height:11px;border-radius:50%;background:#ddd}
.social.second{background:#888}
.bottom{left:0;top:1130px;width:778px;height:70px;background:var(--darker)}
.bottom .copy{position:absolute;left:78px;top:19px;font-size:8px;color:#aaa}
.bottom .legal{position:absolute;left:78px;top:40px;font-size:8px;color:#aaa;word-spacing:1px}
.bottom .round{position:absolute;top:25px;width:21px;height:21px;border:1.5px solid #ddd;border-radius:50%}
</style>
</head>
<body>

<header>
  <div class="abs brand-mark"></div>
  <div class="abs brand-name">Corvane</div>
  <div class="abs btn-login">LOG IN</div>
  <div class="abs btn-register">REGISTER</div>
  <nav class="abs nav">
    <span class="active" style="left:398px">HOME</span>
    <span style="left:455px">ABOUT</span>
    <span style="left:515px">SERVICE</span>
    <span style="left:580px">PRODUCTS</span>
    <span style="left:657px">CONTACT</span>
  </nav>
</header>

<div class="abs hero-band"></div>
<section class="abs hero">
  <div class="abs hero-photo" role="img" aria-label="Businessman in a suit leaning on a railing, looking at his phone above a hazy city"></div>
  <h1 class="abs">Proin a dolor mauris</h1>
  <p class="abs">Curabitur ac elit leo. In eleifend dui tellus, in scelerisque elit porttitor et. Integer eu massa lacinia, lacinia nulla non, volutpat purus.</p>
  <div class="abs read-more">READ MORE</div>
  <div class="abs dots"><i></i><i></i><i></i><i></i></div>
</section>

<h2 class="abs section-title" style="top:402px">WELCOME TO CORVANE</h2>
<p class="abs welcome-text">Donec molestie nisi et tellus hendrerit vehicula. Nunc eu ligula sed quam pulvinar maximus in vitae eros. Proin porta fermen-tum ipsum, vel porttitor turpis venenatis luctus. Vivamus volutpat eu sapien quis tempus. Aenean feugiat viverra lorem ac sagittis. Donec sit amet lectus nec mi tempor laoreet ac nec nunc.</p>
<div class="abs rule"></div>

<h2 class="abs section-title" style="top:542px">OUR SERVICES</h2>
<div class="abs service" style="left:85px">
  <svg width="52" height="50" viewBox="0 0 52 50" fill="#3f4fa3"><path d="M2 14h14a6 6 0 1 1 10 0h12v12a6 6 0 1 1 0 10v12H26a6 6 0 1 0-10 0H2z"/></svg>
  <h3>Pellentesque convallis</h3>
  <p>Curabitur ac elit leo. In eleifend dui tellus, in scelerisque elit porttitor et. Integer eu massa lacinia, lacinia nulla non.</p>
</div>
<div class="abs service" style="left:299px">
  <svg width="54" height="50" viewBox="0 0 54 50" fill="#3f4fa3"><circle cx="12" cy="9" r="7"/><circle cx="42" cy="9" r="7"/><circle cx="27" cy="15" r="9"/><path d="M2 30q0-12 10-12h8v14H2z"/><path d="M52 30q0-12-10-12h-8v14h18z"/><path d="M12 50V36q0-10 15-10t15 10v14z"/></svg>
  <h3>Pellentesque convallis</h3>
  <p>Curabitur ac elit leo. In eleifend dui tellus, in scelerisque elit porttitor et. Integer eu massa lacinia, lacinia nulla non.</p>
</div>
<div class="abs service" style="left:512px">
  <svg width="54" height="50" viewBox="0 0 54 50" fill="#3f4fa3"><rect x="20" y="0" width="14" height="12" rx="1"/><rect x="25.5" y="12" width="3" height="12"/><rect x="6" y="22" width="42" height="3"/><rect x="6" y="22" width="3" height="12"/><rect x="45" y="22" width="3" height="12"/><rect x="25.5" y="22" width="3" height="12"/><rect x="0" y="34" width="14" height="14" rx="1"/><rect x="20" y="34" width="14" height="14" rx="1"/><rect x="40" y="34" width="14" height="14" rx="1"/></svg>
  <h3>Pellentesque convallis</h3>
  <p>Curabitur ac elit leo. In eleifend dui tellus, in scelerisque elit porttitor et. Integer eu massa lacinia, lacinia nulla non.</p>
</div>

<section class="abs team">
  <h2 class="abs section-title" style="top:18px;left:0;width:624px">OUR TEAM</h2>
  <div class="abs member" style="left:16px"><div class="photo" role="img" aria-label="Portrait of a grey-haired man with glasses"></div><div class="name">John Doe</div><div class="role">Non sapien faucibus</div></div>
  <div class="abs member" style="left:138px"><div class="photo" role="img" aria-label="Portrait of an older man with glasses"></div><div class="name">John Doe</div><div class="role">Non sapien faucibus</div></div>
  <div class="abs member" style="left:260px"><div class="photo" role="img" aria-label="Portrait of a smiling woman with auburn hair"></div><div class="name">John Doe</div><div class="role">Non sapien faucibus</div></div>
  <div class="abs member" style="left:382px"><div class="photo" role="img" aria-label="Portrait of a smiling blonde woman"></div><div class="name">John Doe</div><div class="role">Non sapien faucibus</div></div>
  <div class="abs member" style="left:504px"><div class="photo" role="img" aria-label="Portrait of a man with glasses"></div><div class="name">John Doe</div><div class="role">Non sapien faucibus</div></div>
</section>

<footer class="abs footer">
  <h4 style="left:80px">About us</h4>
  <p class="txt" style="left:80px;width:138px">Sed nec enim tempus, porta mi ut, auctor neque. Aliquam ut velit ac nibh vestibulum laoreet. Cras condimentum ut ligula eget rhon-cus. In sit amet odio consequat, lobortis neque quis.</p>
  <div class="divider" style="left:238px"></div>
  <h4 style="left:261px">Testimonials</h4>
  <p class="txt quote" style="left:261px">“ Praesent convallis placerat lorem, quis tincidunt lorem feugiat ut. Morbi ac purus consectetur purus blandit vehicula non a dolor. ”</p>
  <p class="txt" style="left:261px;top:118px">Ned Harlow, NY</p>
  <div class="divider" style="left:432px"></div>
  <h4 style="left:454px">Quick Links</h4>
  <ul class="txt links" style="left:455px;top:50px"><li>Home</li><li>About</li><li>Service</li><li>Product</li><li>Contact</li></ul>
  <div class="divider" style="left:556px"></div>
  <h4 style="left:580px">Newsletter</h4>
  <div class="email">E-mail<b><svg width="27" height="21" viewBox="0 0 27 21"><path d="M10 5l9 5.5-9 5.5z" fill="#888"/></svg></b></div>
  <h4 style="left:580px;top:83px">Follow us on</h4>
  <span class="social" style="left:580px"></span>
  <span class="social second" style="left:606px"></span>
</footer>

<div class="abs bottom">
  <p class="copy">Copyright © 2015 Corvane. All Rights Reserved.</p>
  <p class="legal">Disclaimer | Support | Privacy Policy | Terms of use</p>
  <span class="round" style="left:652px"><svg width="18" height="18" viewBox="0 0 18 18"><rect x="4" y="5.5" width="10" height="7" fill="#fff"/><path d="M4 5.5l5 4 5-4" stroke="#1f1f1f" fill="none"/></svg></span>
  <span class="round" style="left:679px"><svg width="18" height="18" viewBox="0 0 18 18"><path d="M9 4v10M5 8l4-4 4 4" stroke="#ddd" stroke-width="1.6" fill="none"/></svg></span>
</div>

</body>
</html>
```